5 Email Newsletter Templates Needed

We need 5 email templates for our email marketing campaign. We are an Insurance Agency in Los Angeles called KDP-Silverbrook Insurance Services. We use Mailvane Hub as our email marketing platform. The templates need to be simple, a nice header, not to busy and you will need to use our color palette. The first email template we need is for our current clients / prospects. The content we will put in this email will be insurance tips and information, short and simple about 2 small paragraphs. The next 3 templates all need to be the same but different colors. One red, one yellow and one green. These will be alerts from kdp-silverbrook. An example a major earthquake hits we will send a red alert. A legislative change on healthcare and we send a yellow alert. We buy another location and we send a green alert. The last email is for our COINs (Centers of Influence, the people who refer business to us). I uploaded an email from one of our business consultants to give an idea of the size and sophistication we are looking for. I also uploaded our corporate brochure and color palette so you can learn more about our firm.

Target Market(s)

Our target markets are commercial business 1mm plus in revenue, 500 employees, high net worth individuals. Our COINs are CPAs, CFOs, Business Managers

Requirements
Nice to have
• HTML Code is desired. You can also provide just an image file for the header and our email marketing program will do the coding for us.
Should not have
• No cartoon looking graphics. Do not use old-style fonts like Times New Roman.

```html
<!DOCTYPE html>
<html lang="en">
<head>
<meta charset="utf-8">
<title>KDP-Silverbrook Green Alert</title>
<link href="https://fonts.googleapis.com/css2?family=Arimo:wght@400;700&display=swap" rel="stylesheet">
<style>
:root{
  --bg-green:#42861a;
  --alert-green:#3f8c10;
  --brand-teal:#0d5560;
  --heading-red:#d0121b;
  --heading-blue:#135e8d;
  --text:#1a1a1a;
  --rule:#c9c9c9;
  --footer-grey:#d3d3d3;
  --white:#ffffff;
}
*{margin:0;padding:0;box-sizing:border-box}
html,body{width:1013px;height:1200px;overflow:hidden}
body{background:var(--bg-green);font-family:Arimo,Arial,sans-serif;color:var(--text);position:relative}
.browser-link{position:absolute;top:66px;left:0;width:1000px;text-align:center;font-size:10.5px;color:var(--white)}
.card{position:absolute;left:175px;top:85px;width:665px;height:959px;background:var(--white);border-radius:14px;overflow:hidden}
.abs{position:absolute}
.brand{left:26px;top:78px;display:flex;align-items:center;gap:8px;font-size:22px;font-weight:700;color:var(--brand-teal);letter-spacing:1px}
.brand-mark{width:20px;height:20px;background:var(--brand-teal)}
.alert-title{right:25px;top:56px;font-size:24px;font-weight:700;color:var(--alert-green);text-align:right}
.alert-sub{right:25px;top:97px;font-size:14px;font-weight:700;color:#444;text-align:right;line-height:15px}
.header-rule{left:0;top:143px;width:665px;height:1px;background:var(--alert-green)}
.section-title{font-size:16px;color:var(--heading-red);display:flex;align-items:center;gap:6px}
.section-title svg{flex:none}
.rule{height:1px;background:var(--rule)}
.photo{left:26px;top:216px;width:387px;height:182px;background:linear-gradient(180deg,#8a8f96 0%,#4a4f56 55%,#15171a 100%)}
.story-heading{font-size:12.5px;font-weight:700;color:var(--heading-blue)}
.story-body{font-size:12px;line-height:17.3px;width:400px}
.tip-heading{font-size:12px;font-weight:700;color:var(--heading-blue);line-height:14.5px;width:185px}
.tip-body{font-size:12px;line-height:14.5px;width:190px}
.footer{left:0;top:796px;width:665px;height:163px;background:var(--footer-grey);font-size:11px;line-height:14.5px}
.address{left:27px;top:26px}
.web{left:27px;top:112px}
.follow{right:26px;top:16px;display:flex;align-items:center;gap:10px;font-size:10px}
.social{width:23px;height:23px;border-radius:3px;background:#4f78b8}
.social.second{background:#5fb3e0}
.footer-links{right:28px;top:126px;font-size:10px}
.footer-links a{color:var(--text)}
</style>
</head>
<body>
<p class="browser-link">Having trouble reading this newsletter? Click here to view this in a browser.</p>
<main class="card">
  <header>
    <div class="abs brand"><span class="brand-mark"></span>KDP-SILVERBROOK</div>
    <h1 class="abs alert-title">GREEN ALERT!</h1>
    <p class="abs alert-sub">We bought another location<br>Check out a 218 Harmon</p>
    <div class="abs header-rule"></div>
  </header>

  <section>
    <h2 class="abs section-title" style="left:11px;top:175px"><svg width="8" height="14" viewBox="0 0 8 14"><path d="M1 1l6 6-6 6" fill="none" stroke="#d0121b" stroke-width="1.2"/></svg>BUILDING THE FUTURE. TOGETHER.</h2>
    <div class="abs rule" style="left:11px;top:200px;width:409px"></div>
    <div class="abs photo" role="img" aria-label="Photo of modern glass high-rise buildings under a cloudy sky"></div>
    <h3 class="abs story-heading" style="left:26px;top:424px">New Property at 218 Harmon Street</h3>
    <p class="abs story-body" style="left:26px;top:456px">Lorem ipsum dolor sit amet, consectetuer adipiscing elit, sed diam nonummy nibh euismod tincidLorem ipsum dolor sit amet, consectetuer adipiscing elit, sed diam nonummy nibh euismod tincidunt ut laoreet dolore magna aliquam erat volutpat. Ut wisi enim ad minim veniam, quis nostrud exerci tation ullamcorper suscipit lobortis nisl ut utem d exerci tation ullamcorper suscipit lobortis nisl ut aliquip ex ea</p>
    <div class="abs rule" style="left:11px;top:580px;width:409px"></div>
    <h3 class="abs story-heading" style="left:26px;top:602px">COMMERCIAL INSURANCE</h3>
    <p class="abs story-body" style="left:26px;top:633px">Lorem ipsum dolor sit amet, consectetuer adipiscing elit, sed diam nonummy nibh euismod tincidLorem ipsum dolor sit amet, consectetuer adipiscing elit, sed diam nonummy nibh euismod tincidunt ut laoreet dolore magna aliquam erat volutpat. Ut wisi enim ad minim veniam, quis nostrud exerci tation ullamcorper suscipit lobortis nisl ut suscipit lobortis nisl ut aliquip ex ea commodo consequat. Duis autem san et iusto odio dignissim qui blandit praesent luptatum zzril delenit augue duis dolore te feugait nulla facilisi.</p>
  </section>

  <aside>
    <h2 class="abs section-title" style="left:441px;top:175px"><svg width="8" height="14" viewBox="0 0 8 14"><path d="M1 1l6 6-6 6" fill="none" stroke="#d0121b" stroke-width="1.2"/></svg>INSURANCE TIPS</h2>
    <div class="abs rule" style="left:441px;top:200px;width:198px"></div>
    <h3 class="abs tip-heading" style="left:456px;top:216px">Know your state's auto insurance requirements:</h3>
    <p class="abs tip-body" style="left:456px;top:254px">Most states require you to carry a minimum amount of liability coverage. Many states have "no-fault" auto insurance systems. Coverage for medical costs for you and your passengers is optional in some states. Coverage for damage to your car is optional.</p>
    <div class="abs rule" style="left:441px;top:398px;width:198px"></div>
    <h3 class="abs tip-heading" style="left:456px;top:414px">Write up your personal auto insurance profile:</h3>
    <p class="abs tip-body" style="left:456px;top:447px">List pertinent information concerning what type of vehicle you drive, where you drive, who else drives, what your driving record is, where you live, what optional safety features your car has. This profile will make the next step easier.</p>
    <div class="abs rule" style="left:441px;top:580px;width:198px"></div>
    <h3 class="abs tip-heading" style="left:456px;top:600px">Meet with potential insurance agents:</h3>
    <p class="abs tip-body" style="left:456px;top:633px">Make a few appointments, bring your personal auto insurance profile with you, and ask questions. You want a fair price AND quality service. Ask about available discounts, higher deductibles, service options and claims procedures after accidents. Take notes.</p>
  </aside>

  <footer class="abs footer">
    <p class="abs address">KDP - Silverbrook Insurance<br>Services Inc.<br>2250 Marlow Ave. Ste 300<br>Westbrook CA, 90000<br>(555) 014-2260</p>
    <p class="abs web">www.kdp-silverbrook.com<br>info@kdp-silverbrook.com</p>
    <div class="abs follow">FOLLOW KDP SILVERBROOK ON:<span class="social" role="img" aria-label="Social network link"></span><span class="social second" role="img" aria-label="Social network link"></span></div>
    <p class="abs footer-links"><a href="#">Join Our Newsletter</a> | <a href="#">Share this with a Friend</a> | <a href="#">Stop Future Mailings</a></p>
  </footer>
</main>
</body>
</html>
```